Flyer Design Project - law firm

I need a design for an advertising flyer for my law firm.
Ideally the size of the document will be one page A4.
I have attached a copy of the logo. I would like the lettering for 'Marwood Legal' to be all the same size, rather than the 'S' and 'L' being slightly larger
The flyer must include the text below:
Wills
Anyone who owns property or investments or has family obligations should have a Will to ensure that their assets are distributed in accordance with their wishes and that their children are cared for by the guardians of their choosing. Without a Will, these vital decisions are determined by the government or the courts of the State or Territory which you lived in at the time of your death.
Marwood Legal can assist you in the preparation of a legal will tailored to your particular circumstances to ensure that your wishes are followed.
We are offering Tollbeck- Crane Harbour clients a free discussion of their will requirements and a heavily discounted standard wills package of
$330.00* for a single will
$550.00* for couples wills
These prices are only valid prior to your conveyancing settlement for standard wills (e.g. not including a testamentary trust or other complications.
Please contact us on or provide Tollbeck Crane Harbour with authority for us to contact you today.
Updates
Hi All,
I have posted a copy of the proposed logo. Please note that I need the wording of 'Marwood Legal' to all be the same size, rather than the 'S' and 'L' being slightly larger.
If you require anything further please let me know.
Thanks
I have added copies of the logo in ups format,
If you require anything further please let know.
Thanks for your assistance.

```html
<!DOCTYPE html>
<html lang="en">
<head>
<meta charset="utf-8">
<title>Marwood Legal – Wills Flyer</title>
<link href="https://fonts.googleapis.com/css2?family=Bree+Serif&family=Kreon:wght@400;700&family=Montserrat:wght@700&family=Open+Sans:wght@400;700&display=swap" rel="stylesheet">
<style>
  :root {
    --backdrop: #d9d6d2;
    --paper: #ffffff;
    --brown-deep: #4a1a10;
    --brown-title: #5a1f14;
    --brown-wave: #6b3a22;
    --ink: #2b2b2b;
    --ink-soft: #3a3a3a;
    --logo-grey: #3d3d3d;
    --footer-grey: #4a4a4a;
    --photo-dark: #3a2a1c;
    --photo-mid: #8a6a42;
    --photo-light: #e8cf9e;
  }
  * { box-sizing: border-box; margin: 0; padding: 0; }
  html, body {
    width: 1200px; height: 873px; overflow: hidden;
    background: var(--backdrop);
  }
  .flyer {
    position: absolute;
    left: 310px; top: 26px;
    width: 580px; height: 820px;
    background: var(--paper);
    box-shadow: 0 6px 24px rgba(0,0,0,.18);
    overflow: hidden;
  }
  .hero { position: absolute; left: 0; top: 0; width: 580px; height: 290px; }
  .hero-photo {
    position: absolute; inset: 0;
    background: linear-gradient(160deg, var(--photo-light) 0%, var(--photo-mid) 35%, var(--photo-dark) 70%, var(--photo-mid) 100%);
  }
  .hero-wave { position: absolute; left: 0; top: 0; }
  .logo-placeholder {
    position: absolute; right: 36px; top: 268px;
    font-family: "Montserrat", sans-serif; font-weight: 700;
    font-size: 29px; color: var(--logo-grey); letter-spacing: .5px;
  }
  .section-title {
    position: absolute; left: 0; top: 306px;
    padding-left: 36px;
    font-family: "Bree Serif", serif; font-size: 30px; color: var(--brown-title);
  }
  .section-title::before {
    content: ""; position: absolute; left: 0; top: 4px;
    width: 8px; height: 30px; background: var(--brown-deep);
  }
  .intro {
    position: absolute; left: 36px; top: 352px; width: 500px;
    font-family: "Kreon", serif; font-size: 15.5px; line-height: 1.22;
    color: var(--ink); text-align: justify; text-indent: 24px;
  }
  .offer {
    position: absolute; left: 36px; top: 484px; width: 508px;
    font-family: "Open Sans", sans-serif; font-size: 10.3px; line-height: 1.4;
    color: var(--ink-soft);
  }
  .offer strong { font-weight: 700; }
  .price {
    position: absolute; top: 560px; height: 30px;
    background: var(--brown-deep); color: #fff;
    font-family: "Kreon", serif; font-size: 15px;
    display: flex; align-items: center; padding: 0 12px;
  }
  .price strong { font-family: "Bree Serif", serif; font-weight: 400; margin-right: 5px; }
  .price--single { left: 36px; width: 230px; }
  .price--couple { left: 296px; width: 236px; }
  .price-note {
    position: absolute; left: 36px; top: 604px; width: 500px;
    font-family: "Open Sans", sans-serif; font-size: 10.3px; line-height: 1.35;
    color: var(--ink-soft);
  }
  .footer {
    position: absolute; left: 0; bottom: 0; width: 580px; height: 42px;
    background: var(--footer-grey);
    border-top: 3px solid var(--brown-deep);
    display: flex; align-items: center; padding-left: 20px;
    font-family: "Open Sans", sans-serif; font-weight: 700; font-size: 11px; color: #fff;
  }
</style>
</head>
<body>
  <article class="flyer">
    <div class="hero">
      <div class="hero-photo" role="img" aria-label="Photo of a lawyer in a suit leafing through open law books on a desk"></div>
      <svg class="hero-wave" width="580" height="290" viewBox="0 0 580 290" aria-hidden="true">
        <path d="M0 250 C 150 240, 300 225, 420 210 C 490 202, 545 200, 580 198 L580 290 L0 290 Z" fill="var(--brown-wave)"/>
        <path d="M0 262 C 150 252, 300 236, 420 220 C 490 212, 545 210, 580 210 L580 290 L0 290 Z" fill="var(--paper)"/>
      </svg>
    </div>

    <div class="logo-placeholder">LOGO HERE</div>

    <h1 class="section-title">Wills</h1>

    <p class="intro">Anyone who owns property or investments or has family obligations should have a Will to ensure that their assets are distributed in accordance with their wishes and that their children are cared for by the guardians of their choosing. Without a Will, these vital decisions are determined by the government or the courts of the State or Territory which you lived in at the time of your death.</p>

    <p class="offer"><strong>Marwood Legal</strong> can assist you in the preparation of a legal will tailored to your particular circumstances to ensure that your wishes are followed.<br>We are offering Tollbeck- Crane Harbour clients a <strong>free discussion</strong> of their will requirements and a heavily discounted standard wills package of</p>

    <div class="price price--single"><strong>$330.00*</strong> for a single will</div>
    <div class="price price--couple"><strong>$550.00*</strong> for couples wills</div>

    <p class="price-note">These prices are only valid prior to your conveyancing settlement for standard wills (e.g. not including a testamentary trust or other complications.</p>

    <footer class="footer">Please contact us on or provide Tollbeck Crane Harbour with authority for us to contact you today.</footer>
  </article>
</body>
</html>
```